Design einer Kissenverpackung für Blumenmischung zur Stärkung der einheimischen Wildbienen
Zielgruppe
Wir sind ein eCommerce StartUp aus Deutschland, mit Schwerpunkt Samen, Anzuchtsets und Zubehör. Unsere Zielgruppe findet sich in pflanzenaffinen Kunden*innen und im Bereich der Geschenke-Suchenden für Jung und Alt.
Für unser neues Produkt: Eine Blumenmischung zur Stärkung der einheimischen Wildbienen, suchen wir für die vorgegebene Kissenverpackung ein 'Eyecatcher-Design' mit Schwerpunkt 'Wildbiene'
Aufgabenstellung
Es gibt auf diversen Marktplätzen bereits Anbieter die ähnliche Samenmischungen anbieten. Das Design soll also in jedem Fall auffallen um nicht beim Scrollen einfach unterzugehen. Wichtig ist uns der Aspekt 'Wildbiene und deren Schutz'. Das soll besonders hervorgehoben werden. Unsere Samen haben vor allem einheimische Sorten und die Verpackung ist komplett Plastik frei. Der 'Bio' Aspekt ist unserer Zielgruppe und Kunden sehr wichtig, allerdings bitte auf BIO Siegel etc. beim Design verzichten. Unser Logo (beigefügt) soll sich auf unserer Verpackung wiederfinden.
Hier einige Sorten die die Mischung enthält:
- Alexandrinerklee
- Borretsch
- Buchweizen
- Erbse
- Lupine
- Serradella
- Sommerwicke
- Sonnenblume
- etc.
Sonst haben wir erst einmal keine besonderen Vorgaben. Wir haben das Schnittmuster der Druckerei bereits beigefügt. Es gibt 2 Größen, das Design soll auf beiden Verpackungen gleich sein, nur der EAN Code und das Gewicht ändert sich.

```html
<!DOCTYPE html>
<html lang="de">
<head>
<meta charset="utf-8">
<title>Bienen Magnet – Blumenmischung</title>
<link rel="stylesheet" href="https://fonts.googleapis.com/css2?family=Quicksand:wght@400;500;600&display=swap">
<style>
  :root {
    --paper: #ffffff;
    --stripe: #d6e9b4;
    --leaf: #a9cf5c;
    --leaf-dark: #8fbb43;
    --ink: #4a4a4a;
    --white: #ffffff;
    --sun: #f4b321;
    --borage: #6f6fc9;
    --clover: #c9578f;
    --blossom: #e7c3d6;
    --sorrel: #c23c4e;
  }
  * { box-sizing: border-box; margin: 0; padding: 0; }
  html, body {
    width: 1200px; height: 498px; overflow: hidden;
    background: var(--paper);
    font-family: "Quicksand", sans-serif;
  }
  .pack {
    position: relative; width: 1200px; height: 498px; overflow: hidden;
    background: var(--paper);
  }
  .pack__stripes {
    position: absolute; left: 40px; top: 40px; width: 1120px; height: 414px;
    background: repeating-linear-gradient(to bottom,
      var(--stripe) 0 4px, var(--paper) 4px 15px);
  }
  .art { position: absolute; }
  .art--cluster { left: 300px; top: 20px; width: 600px; height: 460px; }
  .art--edge-left { left: 40px; top: 100px; width: 120px; height: 320px; }
  .art--edge-right { left: 1040px; top: 100px; width: 120px; height: 320px; }
  .art--scatter { left: 0; top: 0; width: 1200px; height: 498px; }

  .brand {
    position: absolute; left: 241px; top: 113px; width: 106px; height: 106px;
    border-radius: 50%; background: var(--white);
    border: 2px solid var(--leaf-dark);
    display: flex; align-items: center; justify-content: center;
  }
  .brand__name {
    font-weight: 600; font-size: 18px; color: var(--leaf-dark);
    letter-spacing: 0.5px;
  }

  .seal {
    position: absolute; left: 456px; top: 111px; width: 274px; height: 274px;
    border-radius: 50%; background: var(--leaf);
    display: flex; flex-direction: column; align-items: center; justify-content: center;
    color: var(--white); text-align: center;
  }
  .seal__dots { font-size: 14px; letter-spacing: 8px; line-height: 1; margin: 6px 0; }
  .seal__title {
    font-weight: 400; font-size: 52px; line-height: 1.05; letter-spacing: 4px;
  }
  .seal__sub {
    font-weight: 600; font-size: 10px; letter-spacing: 1.5px; margin-top: 10px;
  }

  .badge {
    position: absolute; left: 868px; top: 306px; width: 88px; height: 88px;
    border-radius: 50%; background: var(--white);
    border: 1.5px solid var(--ink);
    display: flex; align-items: center; justify-content: center;
    text-align: center; color: var(--ink);
    font-weight: 600; font-size: 11px; line-height: 1.2; letter-spacing: 0.5px;
  }
</style>
</head>
<body>
<main class="pack">
  <div class="pack__stripes"></div>

  <svg class="art art--scatter" viewBox="0 0 1200 498" role="img" aria-label="Verstreute Bienen und kleine Wildblüten auf dem Streifengrund">
    <g opacity="0.85">
      <circle cx="185" cy="155" r="16" fill="var(--sun)"/>
      <circle cx="160" cy="240" r="22" fill="var(--sun)"/>
      <circle cx="215" cy="300" r="14" fill="var(--blossom)"/>
      <circle cx="260" cy="260" r="12" fill="var(--borage)"/>
      <circle cx="330" cy="290" r="20" fill="var(--sun)"/>
      <circle cx="365" cy="40" r="10" fill="var(--sun)"/>
      <circle cx="860" cy="90" r="14" fill="var(--sun)"/>
      <circle cx="905" cy="250" r="12" fill="var(--borage)"/>
      <circle cx="945" cy="200" r="12" fill="var(--blossom)"/>
      <circle cx="1000" cy="95" r="14" fill="var(--borage)"/>
      <circle cx="1030" cy="160" r="22" fill="var(--sun)"/>
      <circle cx="985" cy="280" r="14" fill="var(--borage)"/>
      <circle cx="1000" cy="355" r="14" fill="var(--sun)"/>
      <circle cx="940" cy="420" r="16" fill="var(--borage)"/>
      <circle cx="1045" cy="30" r="10" fill="var(--sun)"/>
    </g>
  </svg>

  <svg class="art art--edge-left" viewBox="0 0 120 320" role="img" aria-label="Randstreifen mit Sonnenblumen, Borretsch und Kleeblüten">
    <defs>
      <linearGradient id="edgeLeft" x1="0" y1="0" x2="0" y2="1">
        <stop offset="0" stop-color="var(--clover)"/>
        <stop offset="0.35" stop-color="var(--sun)"/>
        <stop offset="0.7" stop-color="var(--borage)"/>
        <stop offset="1" stop-color="var(--sorrel)"/>
      </linearGradient>
    </defs>
    <rect x="0" y="0" width="120" height="320" rx="50" fill="url(#edgeLeft)" opacity="0.8"/>
  </svg>

  <svg class="art art--edge-right" viewBox="0 0 120 320" role="img" aria-label="Randstreifen mit Sonnenblumen, Borretsch und Kleeblüten">
    <defs>
      <linearGradient id="edgeRight" x1="0" y1="0" x2="0" y2="1">
        <stop offset="0" stop-color="var(--clover)"/>
        <stop offset="0.35" stop-color="var(--sun)"/>
        <stop offset="0.7" stop-color="var(--borage)"/>
        <stop offset="1" stop-color="var(--sorrel)"/>
      </linearGradient>
    </defs>
    <rect x="0" y="0" width="120" height="320" rx="50" fill="url(#edgeRight)" opacity="0.8"/>
  </svg>

  <svg class="art art--cluster" viewBox="0 0 600 460" role="img" aria-label="Blütenkranz aus Sonnenblumen, Borretsch, Klee und Buchweizen mit Bienen rund um das Siegel">
    <defs>
      <radialGradient id="cluster" cx="0.5" cy="0.5" r="0.5">
        <stop offset="0.55" stop-color="var(--sun)"/>
        <stop offset="0.75" stop-color="var(--clover)"/>
        <stop offset="1" stop-color="var(--borage)" stop-opacity="0"/>
      </radialGradient>
    </defs>
    <ellipse cx="293" cy="228" rx="270" ry="225" fill="url(#cluster)" opacity="0.85"/>
  </svg>

  <div class="brand">
    <span class="brand__name">Lunvera</span>
  </div>

  <section class="seal">
    <span class="seal__dots">•••</span>
    <h1 class="seal__title">BIENEN<br>MAGNET</h1>
    <span class="seal__dots">•••</span>
    <p class="seal__sub">BLUMENMISCHUNG</p>
  </section>

  <div class="badge">ZUM<br>SCHUTZ<br>DER<br>BIENEN</div>
</main>
</body>
</html>
```